Business Card Design Project

We need a buisness card for a new digital sinage company. Our target cliants are small to mediaum buisness who want to advertise on out digital sinage network

Target Market(s)

Small to medium buisness

Industry/Entity Type

Digital

Requirements
Must have
• Must have logo

```html
<!DOCTYPE html>
<html lang="en">
<head>
<meta charset="utf-8">
<title>Beacon Business Card</title>
<link rel="stylesheet" href="https://fonts.googleapis.com/css2?family=Ubuntu:wght@400;700&display=swap">
<style>
  :root {
    --page: #ffffff;
    --ink: #111111;
    --white: #ffffff;
    --blue-deep: #4a6f9c;
    --blue-light: #7aa9bf;
    --wave-blue: #4a78a8;
    --wave-orange: #d79a55;
    --gold: #d9b24a;
    --green-deep: #4e8a56;
    --green-light: #b0c493;
    --mark: #3f74b8;
  }
  * { margin: 0; padding: 0; box-sizing: border-box; }
  html, body {
    width: 1200px; height: 1020px; overflow: hidden;
    background: var(--page);
    font-family: "Ubuntu", sans-serif;
  }
  .canvas { position: relative; width: 1200px; height: 1020px; }
  .card { position: absolute; overflow: hidden; }
  .card-front { left: 96px; top: 118px; width: 610px; height: 366px; background: var(--white); }
  .card-back { left: 496px; top: 562px; width: 608px; height: 364px; }
  .card-front .waves { position: absolute; inset: 0; }
  .brand { position: absolute; left: 92px; top: 134px; display: flex; align-items: center; gap: 26px; }
  .brand-square { width: 64px; height: 64px; background: var(--mark); }
  .brand-name { font-weight: 700; font-size: 76px; color: var(--ink); line-height: 1; letter-spacing: -1px; }
  .website { position: absolute; left: 0; width: 100%; top: 330px; padding-left: 2px; text-align: center; font-size: 11px; color: var(--white); }
  .band-top { position: absolute; left: 0; top: 0; width: 100%; height: 62px; background: linear-gradient(90deg, var(--green-deep), var(--green-light)); }
  .band-main { position: absolute; left: 0; top: 62px; width: 100%; height: 207px; background: linear-gradient(90deg, var(--blue-deep), var(--blue-light)); }
  .band-rule { position: absolute; left: 0; top: 269px; width: 100%; height: 13px; background: var(--gold); }
  .band-bottom { position: absolute; left: 0; top: 282px; width: 100%; height: 82px; background: linear-gradient(90deg, var(--green-deep), var(--green-light)); }
  .person-name { position: absolute; left: 319px; top: 86px; font-size: 19px; color: var(--white); }
  .contact { position: absolute; left: 70px; top: 147px; font-size: 17px; line-height: 22px; color: var(--white); list-style: none; }
</style>
</head>
<body>
<div class="canvas">
  <section class="card card-front">
    <svg class="waves" viewBox="0 0 610 366" width="610" height="366">
      <defs>
        <linearGradient id="wave-upper" x1="0" x2="1" y1="0" y2="0">
          <stop offset="0" stop-color="var(--wave-blue)"/>
          <stop offset="0.45" stop-color="#7f8fa0"/>
          <stop offset="1" stop-color="var(--wave-orange)"/>
        </linearGradient>
        <linearGradient id="wave-lower" x1="0" x2="1" y1="0" y2="0">
          <stop offset="0" stop-color="var(--green-deep)"/>
          <stop offset="1" stop-color="#a2b887"/>
        </linearGradient>
      </defs>
      <path d="M0,218 Q260,330 610,198 L610,366 L0,366 Z" fill="url(#wave-upper)"/>
      <path d="M0,290 Q320,302 610,244 L610,366 L0,366 Z" fill="var(--gold)"/>
      <path d="M0,300 Q320,308 610,258 L610,366 L0,366 Z" fill="url(#wave-lower)"/>
    </svg>
    <div class="brand">
      <span class="brand-square"></span>
      <span class="brand-name">Beacon</span>
    </div>
    <p class="website">www.beaconscreens.com.au</p>
  </section>

  <section class="card card-back">
    <div class="band-top"></div>
    <div class="band-main"></div>
    <div class="band-rule"></div>
    <div class="band-bottom"></div>
    <h1 class="person-name" style="font-weight:400">Liam Carver</h1>
    <ul class="contact">
      <li>liam@beaconscreens.com.au</li>
      <li>0400123987</li>
      <li>PO Box 512 Karratha WA 6714</li>
    </ul>
  </section>
</div>
</body>
</html>
```